Online Psychology Practice needs business cards.

Online Psychology service needs business cards. Have own logo- please see uploaded. I have other file formats if you need (not sure one needed?)

Details for Business Card:
Helena Marchetti
Clinical Psychologist BPsych, BPsych (Hons), MPsych (Clin), MAPS
T: 0439627015 | F: 08 73615204
E: hello@brightwatertelehealthcounselling.com.au
W: brightwatertelehealthcounselling.com.au

Industry/Entity Type

Health

Contact Information for Business Card

Logo plus details above (couldn't write in this section)

```html
<!DOCTYPE html>
<html lang="en">
<head>
<meta charset="utf-8">
<title>Brightwater Telehealth Counselling – Business Cards</title>
<link rel="stylesheet" href="https://fonts.googleapis.com/css2?family=Cinzel:wght@600&family=Montserrat:wght@400;500;600&display=swap">
<style>
  :root {
    --navy: #0f3d68;
    --teal: #1b8db0;
    --ink: #3c4650;
    --muted: #6d7882;
    --rule: #9fc6d6;
    --card-white: #ffffff;
    --card-blue: #0b4d7c;
    --card-blue-deep: #073a62;
    --backdrop: #d9dcdf;
  }
  * { box-sizing: border-box; margin: 0; padding: 0; }
  html, body { width: 1200px; height: 800px; overflow: hidden; }
  body {
    background: var(--backdrop);
    display: flex;
    align-items: center;
    justify-content: center;
    gap: 40px;
    font-family: "Montserrat", sans-serif;
  }
  .card {
    position: relative;
    width: 540px;
    height: 310px;
    border-radius: 22px;
    overflow: hidden;
    box-shadow: 0 10px 24px rgba(0,0,0,0.18);
  }
  .card--front { background: var(--card-white); }
  .card--back {
    background: linear-gradient(135deg, var(--card-blue) 0%, var(--card-blue-deep) 100%);
  }

  /* front */
  .brand {
    position: absolute;
    top: 34px;
    right: 34px;
    display: flex;
    align-items: center;
    gap: 10px;
  }
  .brand__dot {
    width: 16px; height: 16px;
    border-radius: 50%;
    background: var(--teal);
  }
  .brand__name {
    font-family: "Cinzel", serif;
    font-weight: 600;
    font-size: 17px;
    line-height: 1.15;
    color: var(--navy);
    letter-spacing: 0.04em;
    text-align: left;
  }
  .contact {
    position: absolute;
    left: 34px;
    bottom: 30px;
  }
  .contact__name {
    font-family: "Cinzel", serif;
    font-weight: 600;
    font-size: 23px;
    color: var(--navy);
    letter-spacing: 0.03em;
  }
  .contact__role {
    font-size: 14px;
    color: var(--teal);
    margin-top: 2px;
  }
  .contact__quals {
    font-size: 9.5px;
    color: var(--muted);
    margin-top: 2px;
  }
  .contact__rule {
    width: 48px;
    height: 1px;
    background: var(--rule);
    margin: 9px 0;
  }
  .contact__line {
    display: flex;
    align-items: center;
    gap: 6px;
    font-size: 12.5px;
    color: var(--ink);
    line-height: 1.6;
  }
  .contact__line svg { width: 11px; height: 11px; fill: var(--teal); flex: none; }
  .contact__web {
    font-size: 12.5px;
    font-weight: 500;
    color: var(--teal);
  }

  /* back */
  .back-brand {
    position: absolute;
    top: 50%;
    left: 50%;
    transform: translate(-50%, -62%);
    display: flex;
    align-items: center;
    gap: 12px;
  }
  .back-brand__dot {
    width: 20px; height: 20px;
    border-radius: 50%;
    background: #dfe5ea;
  }
  .back-brand__name {
    font-family: "Cinzel", serif;
    font-weight: 600;
    font-size: 22px;
    line-height: 1.2;
    color: #dfe5ea;
    letter-spacing: 0.05em;
  }
  .back-web {
    position: absolute;
    left: 0; right: 0;
    bottom: 34px;
    text-align: center;
    color: #ffffff;
    font-size: 14px;
    font-weight: 600;
    letter-spacing: 0.06em;
  }
  .back-web span { font-weight: 400; font-size: 12px; }
</style>
</head>
<body>
  <section class="card card--front" aria-label="Business card front">
    <div class="brand">
      <span class="brand__dot"></span>
      <div class="brand__name">Brightwater<br>Telehealth Counselling</div>
    </div>

    <div class="contact">
      <h1 class="contact__name">HELENA MARCHETTI</h1>
      <p class="contact__role">Clinical Psychologist BPsych,</p>
      <p class="contact__quals">BPsych (Hons), MPsych (Clin), MAPS</p>
      <div class="contact__rule"></div>
      <p class="contact__line">
        <svg viewBox="0 0 24 24" aria-hidden="true"><path d="M6.6 10.8a15 15 0 0 0 6.6 6.6l2.2-2.2a1 1 0 0 1 1-.25 11.4 11.4 0 0 0 3.6.57 1 1 0 0 1 1 1V20a1 1 0 0 1-1 1A17 17 0 0 1 3 4a1 1 0 0 1 1-1h3.5a1 1 0 0 1 1 1c0 1.25.2 2.45.57 3.57a1 1 0 0 1-.25 1z"/></svg>
        0439627015
        <svg viewBox="0 0 24 24" aria-hidden="true"><path d="M6 3h10l2 2v4H6zM4 10h16a2 2 0 0 1 2 2v6h-4v3H6v-3H2v-6a2 2 0 0 1 2-2zm4 6v3h8v-3z"/></svg>
        08 73615204
      </p>
      <p class="contact__line">
        <svg viewBox="0 0 24 24" aria-hidden="true"><path d="M3 5h18v14H3zm2 2v.5l7 4.5 7-4.5V7l-7 4.5z"/></svg>
        hello@brightwatertelehealthcounselling.com.au
      </p>
      <div class="contact__rule"></div>
      <p class="contact__web">brightwatertelehealthcounselling.com.au</p>
    </div>
  </section>

  <section class="card card--back" aria-label="Business card back">
    <div class="back-brand">
      <span class="back-brand__dot"></span>
      <div class="back-brand__name">Brightwater<br>Telehealth Counselling</div>
    </div>
    <p class="back-web">www.BrightwaterTelehealthCounselling<span>.com.au</span></p>
  </section>
</body>
</html>
```